Stationary design for boutique production house

We need a stationary design for our production house, 'Lorin Studios' based in Singapore. We produce microfilms as well as podcasts, talkshows and events. Our logo is a stylized icon of our director, who is also the executive producer and host of our programs, Lorin. Our main company colors are Red, Black and white. We would like a clean, minimalist design incorporating our existing company logo that conveys a sense of urbanism and elegance.

Logo and font files are attached. f

Target Market(s)

We focus on lifestyle media rather than entertainment.

Industry/Entity Type

Boutique

Font styles to use
Serif
Sans Serif

Colors
ec1f27
ffffff
000000

Requirements
Must have
• Our company logo and at least one of our company colors.
Nice to have
• Our address and contact information.
Should not have
• Changes made to the company logo (using only certain parts of it is fine though)

```html
<!DOCTYPE html>
<html lang="en">
<head>
<meta charset="utf-8">
<title>Lorin Studios — Business Card</title>
<link rel="stylesheet" href="https://fonts.googleapis.com/css2?family=Jost:wght@400&display=swap">
<style>
  :root {
    --brand-red: #ec1f27;
    --ink: #231f20;
    --paper: #ffffff;
    --backdrop: #3a3a3a;
    --muted: #555555;
    --faint: #eeeeee;
  }
  * { margin: 0; padding: 0; box-sizing: border-box; }
  html, body {
    width: 1200px; height: 659px; overflow: hidden;
    background: var(--backdrop);
    font-family: "Jost", "Futura", sans-serif;
  }
  .stage {
    position: relative; width: 1200px; height: 659px;
    display: flex; justify-content: center; align-items: center; gap: 60px;
  }
  .card {
    position: relative; width: 300px; height: 525px;
    background: var(--paper); overflow: hidden;
  }
  .card-shape { position: absolute; inset: 0; }

  .brand-name {
    display: flex; align-items: center; gap: 8px; white-space: nowrap;
  }
  .brand-name-text {
    font-family: "Jost", "Futura", sans-serif; font-weight: 400;
    color: var(--ink); letter-spacing: 2px; line-height: 1;
  }
  .brand-mark {
    width: 12px; height: 12px; border-radius: 50%; background: var(--brand-red); flex: none;
  }

  .card-front .brand-name { position: absolute; top: 150px; right: 26px; }
  .card-front .brand-name-text { font-size: 19px; }

  .contact {
    position: absolute; left: 26px; top: 242px; color: var(--paper);
  }
  .contact-name { font-size: 17px; letter-spacing: 0.5px; line-height: 1.2; }
  .contact-role { font-size: 12px; letter-spacing: 0.5px; margin-bottom: 16px; }
  .contact-address { font-size: 11.5px; line-height: 1.4; margin-bottom: 8px; }
  .contact-list { list-style: none; font-size: 11.5px; line-height: 1.55; }
  .contact-list li { display: flex; align-items: center; gap: 8px; }
  .contact-icon { width: 11px; height: 11px; flex: none; }

  .back-brand {
    position: absolute; top: 110px; left: 0; right: 0;
    display: flex; flex-direction: column; align-items: center;
  }
  .card-back .brand-name-text { font-size: 21px; }
  .back-web {
    margin-top: 12px; font-size: 10.5px; letter-spacing: 2.5px; color: var(--muted);
  }
  .back-shape {
    position: absolute; left: 40px; top: 300px; width: 340px; height: 340px;
    border-radius: 50%; background: var(--faint);
  }
</style>
</head>
<body>
<main class="stage">

  <section class="card card-front" aria-label="Business card, front">
    <svg class="card-shape" viewBox="0 0 300 525" aria-hidden="true">
      <path d="M0,195 C150,195 228,300 212,400 C204,455 186,495 178,525 L0,525 Z" fill="var(--ink)"/>
    </svg>

    <div class="brand-name">
      <span class="brand-mark" aria-hidden="true"></span>
      <span class="brand-name-text">LORIN STUDIOS</span>
    </div>

    <div class="contact">
      <p class="contact-name">MARCUS TAN</p>
      <p class="contact-role">CEO/FOUNDER</p>
      <p class="contact-address">18 Keong Saik Road<br>Singapore 089133</p>
      <ul class="contact-list">
        <li>
          <svg class="contact-icon" viewBox="0 0 12 12" aria-hidden="true"><path d="M2.5,1 L4.5,1 L5,3.5 L3.8,4.5 C4.5,6 6,7.5 7.5,8.2 L8.5,7 L11,7.5 L11,9.5 C11,10.5 10,11 9,11 C5,10.5 1.5,7 1,3 C1,2 1.5,1 2.5,1 Z" fill="currentColor"/></svg>
          6221 408 315
        </li>
        <li>
          <svg class="contact-icon" viewBox="0 0 12 12" aria-hidden="true"><rect x="3" y="0.5" width="6" height="11" rx="1" fill="none" stroke="currentColor" stroke-width="1.2"/><circle cx="6" cy="9.5" r="0.7" fill="currentColor"/></svg>
          9174 552 208
        </li>
        <li>
          <svg class="contact-icon" viewBox="0 0 12 12" aria-hidden="true"><rect x="1" y="4" width="10" height="6" fill="currentColor"/><rect x="3" y="1" width="6" height="3" fill="none" stroke="currentColor"/></svg>
          6221 408 316
        </li>
        <li>
          <svg class="contact-icon" viewBox="0 0 12 12" aria-hidden="true"><rect x="0.5" y="2.5" width="11" height="7" fill="currentColor"/><path d="M0.5,2.5 L6,6.5 L11.5,2.5" fill="none" stroke="var(--ink)" stroke-width="1"/></svg>
          hello@lorinstudios.sg
        </li>
        <li>
          <svg class="contact-icon" viewBox="0 0 12 12" aria-hidden="true"><circle cx="6" cy="6" r="5" fill="none" stroke="currentColor" stroke-width="1.2"/><path d="M1,6 H11 M6,1 C3.5,4 3.5,8 6,11 M6,1 C8.5,4 8.5,8 6,11" fill="none" stroke="currentColor" stroke-width="0.9"/></svg>
          www.lorinstudios.sg
        </li>
      </ul>
    </div>
  </section>

  <section class="card card-back" aria-label="Business card, back">
    <div class="back-shape" aria-hidden="true"></div>
    <div class="back-brand">
      <div class="brand-name">
        <span class="brand-mark" aria-hidden="true"></span>
        <span class="brand-name-text">LORIN STUDIOS</span>
      </div>
      <p class="back-web">www.lorinstudios.sg</p>
    </div>
  </section>

</main>
</body>
</html>
```